PowerPoint Design Project

We've recently updated our logo and we are in the processing of updating our web sites, business cards, letterhead, etc.

We're looking for a complete redesign of our Powerpoint template, which we have attached for reference.

Unfortunately our new web site is not released and is currently undergoing redesign so we can't send you a link to inspire.

Also attached here is our new logo.

Target Market(s)

Executives, Ph.D. scientists, researchers, venture capitalists, Board members

Industry/Entity Type

Business

```html
<!DOCTYPE html>
<html lang="en">
<head>
<meta charset="UTF-8">
<title>Presentation Title Slide</title>
<link rel="stylesheet" href="https://fonts.googleapis.com/css2?family=Noto+Sans:wght@400;700&family=Varela+Round&display=swap">
<style>
  :root {
    --brand-blue: #0a8fc6;
    --text-grey: #7a7a7a;
    --wordmark-grey: #5f6366;
    --frame-line: #8fbcd9;
    --paper: #ffffff;
  }
  html, body {
    margin: 0;
    padding: 0;
    overflow: hidden;
    background: var(--paper);
  }
  .slide {
    position: relative;
    width: 1200px;
    height: 901px;
    overflow: hidden;
    background: var(--paper);
    box-sizing: border-box;
    border: 2px solid var(--frame-line);
    font-family: "Noto Sans", sans-serif;
  }
  .decor {
    position: absolute;
    inset: 0;
    width: 1200px;
    height: 901px;
  }
  .brand {
    position: absolute;
    left: 28px;
    top: 22px;
    display: flex;
    align-items: center;
    gap: 16px;
  }
  .brand-dot {
    width: 62px;
    height: 62px;
    border-radius: 50%;
    background: var(--brand-blue);
  }
  .brand-name {
    font-family: "Varela Round", sans-serif;
    font-size: 56px;
    line-height: 1;
    color: var(--wordmark-grey);
    letter-spacing: 0.5px;
  }
  .title {
    position: absolute;
    left: 772px;
    top: 106px;
    width: 440px;
    margin: 0;
    text-align: center;
    font-weight: 700;
    font-size: 50px;
    line-height: 64px;
    color: var(--text-grey);
  }
  .subtitle {
    position: absolute;
    left: 696px;
    top: 584px;
    width: 440px;
    margin: 0;
    text-align: center;
    font-weight: 400;
    font-size: 48px;
    line-height: 63px;
    color: var(--text-grey);
  }
</style>
</head>
<body>
  <main class="slide">
    <svg class="decor" viewBox="0 0 1200 901" aria-hidden="true">
      <circle class="ring" cx="970" cy="218" r="264" fill="none" stroke="var(--brand-blue)" stroke-width="64"/>
      <circle class="disc" cx="254" cy="607" r="345" fill="var(--brand-blue)"/>
    </svg>

    <div class="brand">
      <span class="brand-dot"></span>
      <span class="brand-name">HelixSeek</span>
    </div>

    <h1 class="title">Presentation<br>Title<br>Slide</h1>
    <p class="subtitle">Presentation<br>subtitle goes<br>here.</p>
  </main>
</body>
</html>
```